Cybersecurity company is looking for business card.

I need a business card design for our company, we are a cybersecurity company providing advance technology to protect agains any kind of malware. We need a fresh modern design it should communicate modern, technology and growth.

Target Market(s)

Business to business

Industry/Entity Type

Business

Contact Information for Business Card

Should have location, address, fax, mobile, phone, email and website.

Requirements
Must have
• Must follow company's logo color and style. Must have the company's log on its.

```html
<!DOCTYPE html>
<html lang="en">
<head>
<meta charset="utf-8">
<title>Vantorel – Business Card</title>
<link href="https://fonts.googleapis.com/css2?family=Exo+2:wght@500;700;800&family=Lato:wght@400;700;900&family=Noto+Serif:wght@400&display=swap" rel="stylesheet">
<style>
  :root {
    --bg: #2a2a2a;
    --card-white: #f4f4f4;
    --ink: #141414;
    --black: #0b0b0b;
    --red: #a3121a;
    --red-light: #d0303a;
    --grey: #c9c9c9;
  }
  * { margin: 0; padding: 0; box-sizing: border-box; }
  html, body { width: 1200px; height: 873px; overflow: hidden; }
  body {
    background: var(--bg);
    position: relative;
    font-family: "Lato", sans-serif;
  }
  .card {
    position: absolute;
    width: 560px;
    height: 320px;
    border-radius: 24px;
    overflow: hidden;
    box-shadow: 0 18px 40px rgba(0,0,0,.55);
  }
  /* Front */
  .card-front {
    left: 70px; top: 90px;
    background: linear-gradient(160deg, #ffffff 0%, var(--card-white) 60%, #e4e4e4 100%);
    display: flex; flex-direction: column; align-items: center; justify-content: center;
  }
  .brand-name {
    font-family: "Exo 2", sans-serif;
    font-weight: 800;
    color: var(--ink);
    letter-spacing: 1px;
    line-height: 1;
  }
  .card-front .brand-name { font-size: 64px; }
  .tagline {
    font-family: "Exo 2", sans-serif;
    font-weight: 500;
    color: var(--red);
    font-size: 24px;
    letter-spacing: 1px;
    margin-top: 4px;
  }
  /* Back */
  .card-back {
    left: 570px; top: 470px;
    background: var(--card-white);
  }
  .card-back svg.bands { position: absolute; inset: 0; }
  .card-back .brand-name {
    position: absolute; left: 30px; top: 52px;
    font-size: 48px;
  }
  .person {
    position: absolute; left: 180px; top: 150px; width: 250px;
    text-align: center; color: #fff;
  }
  .person-name { font-weight: 900; font-size: 19px; line-height: 1.1; }
  .person-role { font-weight: 400; font-size: 14px; }
  .office {
    position: absolute; right: 26px; top: 190px; text-align: right;
  }
  .office-name { color: var(--grey); font-size: 16px; letter-spacing: .5px; margin-bottom: 6px; }
  .office-address { color: var(--red); font-weight: 700; font-size: 13px; line-height: 1.3; }
  .contacts {
    position: absolute; left: 26px; top: 222px; list-style: none;
    font-family: "Noto Serif", serif; color: #e8e8e8; font-size: 15px; line-height: 20px;
  }
  .contacts li { display: flex; align-items: center; gap: 10px; }
  .contacts svg { width: 12px; height: 12px; fill: var(--red); flex: none; }
</style>
</head>
<body>

  <section class="card card-front" aria-label="Card front">
    <div class="brand-name">vantorel</div>
    <div class="tagline">cybersecurity company</div>
  </section>

  <section class="card card-back" aria-label="Card back">
    <svg class="bands" viewBox="0 0 560 320" preserveAspectRatio="none" aria-hidden="true">
      <polygon points="0,200 560,150 560,320 0,320" fill="var(--black)"/>
      <polygon points="0,188 150,176 180,150 430,128 460,118 560,110 560,122 470,130 440,148 200,170 170,196 0,210" fill="var(--red-light)"/>
      <polygon points="150,176 180,150 430,128 440,148 200,170 170,196" fill="var(--red)"/>
      <polygon points="0,200 170,196 200,170 440,148 560,138 560,150 0,212" fill="var(--red)"/>
    </svg>
    <div class="brand-name">vantorel</div>
    <div class="person">
      <div class="person-name">Daniel Koval</div>
      <div class="person-role">Owner / Founder</div>
    </div>
    <div class="office">
      <div class="office-name">VANTOREL</div>
      <div class="office-address">Harbor Tech Park (HTP)<br>-Marina Crest Road.</div>
    </div>
    <ul class="contacts">
      <li><svg viewBox="0 0 12 12"><rect x="3" y="0" width="6" height="12" rx="1.2"/></svg>3571204466</li>
      <li><svg viewBox="0 0 12 12"><path d="M1 4c0-2 2-3 5-3s5 1 5 3l-2 1-1-2H4L3 5zM2 6h8l1 5H1z"/></svg>3879031257</li>
      <li><svg viewBox="0 0 12 12"><rect x="3" y="0" width="6" height="4"/><rect x="0" y="4" width="12" height="7" rx="1"/></svg>3362418850</li>
      <li><svg viewBox="0 0 12 12"><rect x="0" y="2" width="12" height="8" rx="1"/></svg>name.surname@vantorel.com</li>
    </ul>
  </section>

</body>
</html>
```